Donation Banner for Briarcrest High School Entrances

Create a banner to be hung at entrances at the school, to encourage participation in donation campaign.

See examples on attached document. What I like about the sampes: clean, easy to read, clear, mission-oriented.

Briarcrest Rd
Desired Size 100”w x 70”h

Castellan Rd Entrance
Desired Size 70”w x 50”h

Target Market(s)

Parents from the school and community members driving by. Silicon Valley professionals.

Font styles to use
Sans Serif

Colors
f78f20
9bcb3c
0393ce

Requirements
Must have
• School colors are orange and black. We can introduce small amounts of another color - maybe green to encourage donations. Or blue as it is opposite of orange on the color wheel.
• Banner must track dollar $$$ goal tracking up to $1.1M, in 200K increments (or whatever looks good) not %
• Our goal is 1.1M.
• Arrow Up, not thermometer.
• List website: bhsfoundation-example.org.
• Include round Briarcrest Foundation logo, see file provided.
• Must include mission oriented messaging: Reduced Class Sizes, Expanded Electives, Student Support
• Our Organization is Briarcrest High School Foundation, must be listed

```html
<!DOCTYPE html>
<html lang="en">
<head>
<meta charset="utf-8">
<title>Briarcrest High School Foundation – Donation Banner</title>
<link rel="stylesheet" href="https://fonts.googleapis.com/css2?family=Anton&family=Oswald:wght@500;700&display=swap">
<style>
  :root {
    --orange: #ea8a2c;
    --orange-deep: #e07b1f;
    --orange-soft: #f7b25a;
    --sun: #fcd36a;
    --headline: #fde36a;
    --white: #ffffff;
    --ink: #1a1a1a;
    --red: #e42b2b;
  }
  * { margin: 0; padding: 0; box-sizing: border-box; }
  html, body { width: 1200px; height: 840px; overflow: hidden; background: var(--white); }
  .banner { position: relative; width: 1200px; height: 840px; font-family: "Oswald", sans-serif; }

  .brand-band { position: absolute; inset: 0 0 auto 0; height: 202px; background: var(--white);
    display: flex; align-items: center; justify-content: center; gap: 22px; }
  .brand-mark { width: 64px; height: 64px; border-radius: 50%; background: var(--orange); }
  .brand-name { font-family: "Oswald", sans-serif; font-weight: 700; font-size: 38px;
    letter-spacing: 2px; text-transform: uppercase; color: var(--ink); }

  .field { position: absolute; left: 0; right: 0; top: 202px; bottom: 0; overflow: hidden;
    background:
      radial-gradient(circle at 917px 80px, var(--sun) 0%, var(--orange-soft) 22%, rgba(234,138,44,0) 55%),
      linear-gradient(90deg, var(--orange-deep), var(--orange)); }

  .headline { position: absolute; left: 33px; top: 86px; font-family: "Anton", sans-serif;
    font-size: 62px; line-height: 1; color: var(--headline); letter-spacing: 0.5px;
    text-shadow: 2px 2px 0 var(--white), 4px 5px 6px rgba(120,50,0,0.45); }

  .missions-title { position: absolute; left: 42px; width: 618px; top: 203px;
    display: flex; align-items: center; gap: 22px; color: var(--white);
    font-weight: 700; font-size: 33px; letter-spacing: 1px; }
  .missions-title::before, .missions-title::after { content: ""; flex: 1; height: 4px; background: var(--white); }

  .missions { position: absolute; left: 30px; top: 267px; display: flex; gap: 15px; list-style: none; }
  .mission { width: 190px; display: flex; flex-direction: column; align-items: center; }
  .mission-badge { width: 186px; height: 186px; border-radius: 50%; background: var(--white);
    display: flex; align-items: center; justify-content: center; }
  .mission-icon { width: 112px; height: 100px; border-radius: 16px; background: var(--orange); }
  .mission-label { margin-top: 22px; color: var(--white); font-weight: 500; font-size: 25px; white-space: nowrap; }

  .website { position: absolute; left: 33px; top: 548px; display: flex; align-items: center; gap: 22px;
    color: var(--white); font-weight: 700; font-size: 36px; }
  .website svg { width: 54px; height: 54px; }

  .goal { position: absolute; left: 700px; top: 0; width: 400px; height: 638px; }
  .goal svg { position: absolute; left: 0; top: 0; }
  .goal-amount { position: absolute; left: 17px; width: 400px; top: 96px; text-align: center;
    font-family: "Anton", sans-serif; font-size: 64px; line-height: 1; color: var(--headline);
    text-shadow: 2px 2px 0 var(--white), 4px 5px 6px rgba(120,50,0,0.45); }
  .tick { position: absolute; font-family: "Oswald", sans-serif; font-weight: 700; color: var(--white);
    line-height: 1; white-space: nowrap; }
  .tick.left { right: 214px; text-align: right; }
  .tick.right { left: 255px; }
  .t880 { top: 262px; font-size: 40px; }
  .t660 { top: 366px; font-size: 33px; }
  .t440 { top: 470px; font-size: 27px; }
  .t220 { top: 570px; font-size: 17px; }
</style>
</head>
<body>
<main class="banner">
  <header class="brand-band">
    <span class="brand-mark"></span>
    <span class="brand-name">Briarcrest High School Foundation</span>
  </header>

  <section class="field">
    <h1 class="headline">Help Us Reach Our Target</h1>

    <h2 class="missions-title">MISSIONS</h2>
    <ul class="missions">
      <li class="mission">
        <div class="mission-badge"><div class="mission-icon" role="img" aria-label="Icon of students seated at desks"></div></div>
        <span class="mission-label">Reduced Class Sizes</span>
      </li>
      <li class="mission">
        <div class="mission-badge"><div class="mission-icon" role="img" aria-label="Icon of a stack of books"></div></div>
        <span class="mission-label">Expanded Electives</span>
      </li>
      <li class="mission">
        <div class="mission-badge"><div class="mission-icon" role="img" aria-label="Icon of hands supporting a graduate"></div></div>
        <span class="mission-label">Student Support</span>
      </li>
    </ul>

    <p class="website">
      <svg viewBox="0 0 54 54" aria-hidden="true">
        <circle cx="27" cy="27" r="26" fill="#fff"/>
        <path d="M14 14c6 2 8 6 6 10s2 8 6 8 2 8-2 12c-8-3-14-10-14-17 0-5 2-9 4-13z" fill="#ea8a2c"/>
        <path d="M32 6c2 4 8 4 10 8s-2 6 2 10 2 10 0 14c-4-2-6-6-4-10s-6-4-6-10 0-8-2-12z" fill="#ea8a2c"/>
      </svg>
      www.bhsfoundation-example.org
    </p>

    <div class="goal">
      <svg width="400" height="638" viewBox="0 0 400 638" aria-hidden="true">
        <path d="M217 173 L283 245 L242 245 L242 545 Q244 610 268 638 L166 638 Q190 610 192 545 L192 245 L150 245 Z" fill="#fff"/>
        <path d="M207 485 L228 485 L228 572 Q230 615 246 638 L188 638 Q205 615 207 572 Z" fill="var(--red)"/>
      </svg>
      <div class="goal-amount">$1.1M</div>
      <span class="tick left t880">880K</span><span class="tick right t880">880K</span>
      <span class="tick left t660">660K</span><span class="tick right t660">660K</span>
      <span class="tick left t440">440K</span><span class="tick right t440">440K</span>
      <span class="tick left t220">220K</span><span class="tick right t220">220K</span>
    </div>
  </section>
</main>
</body>
</html>
```